Gobal construction supply company needs new business card design

I need a business card design for my global supply company using an existing logo. i will be looking to print these on rounded corner cards with the black background version of my logo on the back. on the front white background, my logo again and my simple details.

```html
<!DOCTYPE html>
<html lang="en">
<head>
<meta charset="utf-8">
<title>Meridian Build Supply — Business Card</title>
<link rel="stylesheet" href="https://fonts.googleapis.com/css2?family=Bebas+Neue&family=Work+Sans:wght@400;500;600&display=swap">
<style>
  :root {
    --backdrop: #1c1c1d;
    --card: #141415;
    --card-edge: #242426;
    --ink: #f4f4f4;
    --accent: #e01b24;
  }
  * { margin: 0; padding: 0; box-sizing: border-box; }
  html, body {
    width: 1200px; height: 900px; overflow: hidden;
    background: var(--backdrop);
  }
  .stage {
    width: 1200px; height: 900px;
    display: flex; flex-direction: column; align-items: center; justify-content: center;
    gap: 50px;
  }
  .card {
    position: relative;
    width: 630px; height: 360px;
    border-radius: 14px;
    background: linear-gradient(135deg, var(--card) 0%, #1b1b1c 60%, #262628 100%);
    box-shadow: 0 0 0 1px var(--card-edge);
    color: var(--ink);
    font-family: "Work Sans", sans-serif;
  }
  /* Front: brand */
  .card--brand { display: flex; align-items: center; justify-content: center; }
  .brand { display: flex; align-items: center; gap: 14px; }
  .brand__name {
    font-family: "Work Sans", sans-serif;
    font-weight: 600; font-size: 27px; letter-spacing: 1.5px;
    text-transform: uppercase; color: var(--ink);
  }
  .brand__dot { width: 18px; height: 18px; border-radius: 50%; background: var(--accent); }

  /* Back: details */
  .identity {
    position: absolute; left: 0; top: 132px; width: 262px;
    text-align: right;
  }
  .identity__name {
    font-family: "Bebas Neue", sans-serif;
    font-size: 44px; line-height: 0.95; letter-spacing: 0.5px;
    color: var(--accent);
  }
  .identity__role { font-size: 16px; letter-spacing: 1px; margin-top: 4px; }
  .divider {
    position: absolute; left: 285px; top: 140px;
    width: 2px; height: 62px; background: var(--ink);
  }
  .contact {
    position: absolute; left: 308px; top: 136px;
    list-style: none; display: flex; flex-direction: column; gap: 5px;
  }
  .contact__item {
    display: flex; align-items: center; gap: 10px;
    font-size: 16px; letter-spacing: 1.2px;
  }
  .contact__icon { width: 12px; height: 12px; flex: none; }
  .address {
    position: absolute; left: 50px; bottom: 48px;
    font-size: 18px; letter-spacing: 1.3px;
  }
</style>
</head>
<body>
<main class="stage">
  <section class="card card--brand" aria-label="Card front">
    <div class="brand">
      <span class="brand__name">Meridian Build Supply</span>
      <span class="brand__dot" aria-hidden="true"></span>
    </div>
  </section>

  <section class="card card--details" aria-label="Card back">
    <div class="identity">
      <h1 class="identity__name">Daniel Carter</h1>
      <p class="identity__role">Director</p>
    </div>
    <div class="divider" aria-hidden="true"></div>
    <ul class="contact">
      <li class="contact__item">
        <svg class="contact__icon" viewBox="0 0 12 12" aria-hidden="true"><path d="M2.5 1 L4.5 1 L5 3.5 L3.8 4.4 Q4.8 6.8 7.6 8.2 L8.5 7 L11 7.5 L11 9.5 Q11 11 9.5 11 Q1 10 1 2.5 Q1 1 2.5 1 Z" fill="var(--accent)"/></svg>
        403-555-0182
      </li>
      <li class="contact__item">
        <svg class="contact__icon" viewBox="0 0 12 12" aria-hidden="true"><rect x="1" y="2.5" width="10" height="7" fill="none" stroke="var(--accent)" stroke-width="1.2"/><path d="M1 2.5 L6 6.5 L11 2.5" fill="none" stroke="var(--accent)" stroke-width="1.2"/></svg>
        info@meridianbuild.com
      </li>
      <li class="contact__item">
        <svg class="contact__icon" viewBox="0 0 12 12" aria-hidden="true"><g fill="none" stroke="var(--accent)" stroke-width="1"><circle cx="6" cy="6" r="5"/><ellipse cx="6" cy="6" rx="2.2" ry="5"/><path d="M1 6 H11 M2 3.3 H10 M2 8.7 H10"/></g></svg>
        www.meridianbuild.com
      </li>
    </ul>
    <p class="address">48 Harbour Road Box 512, Eastvale, AB</p>
  </section>
</main>
</body>
</html>
```